Design new Brackwater Asset business card 2016

We need a new business card for our company Brackwater Asset Partners. We are a niche Alternative Investment Fund Manager based in Chester, in the North West of the UK.We market our services to global institutions such as banks, insurance companies, pension funds, etc. as well as wealthy individuals. Our main markets are Europe (Germany\France\Switzerland), the US and parts of Asia.
The design needs to be in line with existing company branding. Life the assets we deal with, the business card might suggest, "niche\alternative" type of attributes - however, it needs to remain professional, clean and appropriate for our client base.
Our existing business card format with relevant factual information is included, along with logo and branding details.

Target Market(s)

We market our services to global institutions such as banks, insurance companies, pension funds, etc. as well as wealthy individuals.

Industry/Entity Type

Financial Service

Contact Information for Business Card

please see attached pdf for information on existing business card which we should aim to convey on your new design. However:
- the wording "Brackwater Asset Partners Ltd is Authorised and Regulated
by the Monetary Oversight Bureau. Registered No. 7139046" should be replaced with , "Brackwater Asset Partners Ltd is an Alternative Investment Fund Manager Authorised and Regulated by the Monetary Oversight Bureau. Registered No. 7139046"
- the "reception" word on reverse can be omitted.
- the "retail: www.toplivanex.co.uk" wording can be omitted.
- the QR code is not required in the new version.

Font styles to use
Serif
Sans Serif

Requirements
Must have
• information on current business card, subject to comments provided above.
Nice to have
• Use of areas of solid colour instead of large areas of white space might be nice to experiment with. However, still need to have the general look and feel of the brand as presented on our website www.bwfundco.co.uk
• If we had space for 3 bullet points describing what we do\who we are, this might be good to try out. e.g. alternative investment fund manager, longevity specialist, founded 1990.
• Also, we have a new tag line, "expertise with longevity" which might fit nicely somewhere on the business card.
Should not have
• - no QR code
• - should not use all the colours in our logo as it looks very garish! Using one or two colours with black\white etc, seems to work better.

```html
<!DOCTYPE html>
<html lang="en">
<head>
<meta charset="utf-8">
<title>Brackwater Asset Partners – Business Card</title>
<link rel="stylesheet" href="https://fonts.googleapis.com/css2?family=Open+Sans:wght@400;600;700&family=Libre+Baskerville:wght@700&display=swap">
<style>
  :root {
    --backdrop: #2b2b2b;
    --card: #050505;
    --blue: #2ea6df;
    --gold: #a8964a;
    --mosaic-a: #c9a230;
    --mosaic-b: #7a5a3a;
    --mosaic-c: #d8324a;
    --mosaic-d: #3fb0e0;
  }
  * { margin: 0; padding: 0; box-sizing: border-box; }
  html, body { width: 1200px; height: 900px; overflow: hidden; }
  body {
    background: var(--backdrop);
    font-family: "Open Sans", Arial, sans-serif;
    position: relative;
  }
  .card {
    position: absolute;
    left: 290px;
    width: 620px;
    height: 354px;
    background: var(--card);
    border-radius: 18px;
    overflow: hidden;
  }
  .card--front { top: 60px; }
  .card--back { top: 486px; border-bottom: 2px solid var(--blue); }

  /* front */
  .services {
    position: absolute; right: 34px; top: 34px;
    display: flex; align-items: flex-start; gap: 10px;
  }
  .services__list {
    list-style: none; text-align: right;
    color: var(--blue); font-size: 13px; line-height: 16px;
  }
  .services__dots { display: flex; flex-direction: column; gap: 3px; padding-top: 2px; }
  .services__dots span {
    width: 12px; height: 10px; border-radius: 50%; background: var(--gold); display: block;
  }
  .brand-mark {
    position: absolute; left: 48px; top: 100px; width: 180px;
    display: flex; flex-direction: column; align-items: center; gap: 12px;
  }
  .brand-mark__dot {
    width: 120px; height: 120px; border-radius: 50%; background: var(--gold);
  }
  .brand-mark__name {
    color: var(--blue); font-size: 14px; font-weight: 400; text-align: center;
  }
  .founded {
    position: absolute; left: 48px; top: 282px; width: 180px; text-align: center;
    color: var(--blue); font-size: 14px;
  }
  .company {
    position: absolute; left: 232px; right: 20px; top: 166px; text-align: center;
  }
  .company__name {
    color: var(--gold); font-size: 22px; font-weight: 700; letter-spacing: 0.5px;
    margin-bottom: 14px;
  }
  .company__address, .company__web {
    color: var(--blue); font-size: 12.5px; line-height: 18px;
  }
  .company__reg {
    color: var(--blue); font-size: 11.5px; line-height: 15px; margin-top: 12px;
  }

  /* back */
  .pattern-strip {
    position: absolute; left: 0; top: 0; bottom: 0; width: 96px;
    background: linear-gradient(160deg, var(--mosaic-c), var(--mosaic-a) 35%, var(--mosaic-b) 65%, var(--mosaic-d));
  }
  .lockup {
    position: absolute; left: 124px; top: 38px;
    display: flex; align-items: center; gap: 14px;
  }
  .lockup__dot { width: 66px; height: 66px; border-radius: 50%; background: var(--gold); }
  .lockup__name { color: var(--gold); font-size: 20px; font-weight: 400; line-height: 24px; }
  .tagline {
    position: absolute; left: 204px; top: 112px;
    font-family: "Libre Baskerville", Georgia, serif; font-weight: 700;
    color: var(--blue); font-size: 12px; letter-spacing: 0.3px;
  }
  .rule { position: absolute; height: 2px; background: var(--blue); right: 0; }
  .rule--top { left: 204px; top: 134px; }
  .rule--mid { left: 124px; top: 262px; }
  .person { position: absolute; left: 124px; top: 196px; }
  .person__name { color: var(--blue); font-size: 26px; font-weight: 700; line-height: 30px; }
  .person__title { color: var(--gold); font-size: 14px; line-height: 20px; }
  .contacts { position: absolute; left: 124px; top: 272px; list-style: none; }
  .contacts li {
    display: flex; align-items: center; gap: 12px;
    color: var(--blue); font-size: 14px; line-height: 22px;
  }
  .contacts svg { width: 14px; height: 14px; flex: none; }
</style>
</head>
<body>

<section class="card card--front" aria-label="Card front">
  <div class="services">
    <ul class="services__list">
      <li>Alternative Investment</li>
      <li>Fund Manager</li>
      <li>Longevity Specialist</li>
    </ul>
    <div class="services__dots"><span></span><span></span><span></span></div>
  </div>

  <div class="brand-mark">
    <div class="brand-mark__dot"></div>
  </div>
  <p class="founded">Founded 1990.</p>

  <div class="company">
    <h1 class="company__name">BRACKWATER ASSET PARTNERS</h1>
    <p class="company__address">14-16 Larkmoor Yard | Wexley Row | Chester | CH2 9QT | UK</p>
    <p class="company__web">www.bwfundco.co.uk</p>
    <p class="company__reg">Brackwater Asset Partners Ltd is an Alternative Investment Fund Manager Authorised<br>and Regulated by the Monetary Oversight Bureau. Registered No. 7139046</p>
  </div>
</section>

<section class="card card--back" aria-label="Card back">
  <div class="pattern-strip" role="img" aria-label="Colourful stained-glass style mosaic pattern strip"></div>

  <div class="lockup">
    <div class="lockup__dot"></div>
    <p class="lockup__name">Brackwater Asset Partners</p>
  </div>
  <p class="tagline">EXPERTISE WITH LONGEVITY</p>
  <div class="rule rule--top"></div>

  <div class="person">
    <h2 class="person__name">DANIEL MERROW</h2>
    <p class="person__title">Non-Executive Chairman</p>
  </div>
  <div class="rule rule--mid"></div>

  <ul class="contacts">
    <li>
      <svg viewBox="0 0 16 16" aria-hidden="true"><path d="M3 2h3l1 3-2 1.5a9 9 0 0 0 4.5 4.5L11 9l3 1v3a1 1 0 0 1-1 1A12 12 0 0 1 2 3a1 1 0 0 1 1-1z" fill="none" stroke="#a8964a" stroke-width="1.4"/></svg>
      +44 (0)1632 960418
    </li>
    <li>
      <svg viewBox="0 0 16 16" aria-hidden="true"><rect x="4" y="1.5" width="8" height="13" rx="1.5" fill="none" stroke="#a8964a" stroke-width="1.4"/><circle cx="8" cy="12" r="0.9" fill="#a8964a"/></svg>
      +44 (0)7700 900527
    </li>
    <li>
      <svg viewBox="0 0 16 16" aria-hidden="true"><rect x="1.5" y="3.5" width="13" height="9" rx="1" fill="none" stroke="#a8964a" stroke-width="1.4"/><path d="M2 4l6 5 6-5" fill="none" stroke="#a8964a" stroke-width="1.4"/></svg>
      dmerrow@bwfundco.co.uk
    </li>
  </ul>
</section>

</body>
</html>
```